Organic Herbs & Spices container

Greek startup company, which cultivate and trade spices and herbs (such as oregano, mint, thyme, sage etc.)

At present we are interested in only the type and shape of packaging which should be made by materials such as paper, cardboard, laminated paper and others based on paper or plastic.

Package size vary from 80g (2.82oz) - 300g (10.58oz). We are going to use the same packing for a variety of products with different information

* Please find attached our logo which should be included in the design.
* There is no company name available at the moment, however a name placeholder should be included.
* include a placeholder for the type of product (sage, oregano, mint, tea etc...).
* Each package should have a place in order to include product details and nutrition facts.

e.g.
xxxx (company name placeholder)
Sage (product type)
product details and nutrition facts.
Updates

Dear designers,first of all, thank you for your proposals. Please find bellow some updates for the project.- It is mandatory to include the logo into the design - Each package should be able to stored vertically - We are looking for one specific package design, please do not submit many variations of a certain package neither colour differentiations Thanks and good luck Added Wednesday, September 28, 2016

Please avoid the use of images. The same package will be used for all the kinds of products (only name and maybe colour will be different among different products. A transparent frame that will show the contents could be used too) Added Wednesday, September 28, 2016

Please find attached logo in EPS format

Our logo is the baseline, any concepts should be based on it. Try to avoid just adding the logo as a small sticker somewhere on the design. Please try to create around it at any way toy like. This could be, to visualize it as a 3D shape or object which can be used as the container of the products.

Reason: We would like to extend the time of the project. We believe that most of the submitted designs do not comply with our requirements.

Reason: We would like to see a bigger variety of ideas

Target Market(s)

Pretty much to anyone over 20 years old worldwide.

Industry/Entity Type

Nutrition

Requirements
Must have
• It should be attractive, easily recognized, simple yet innovative, durable, functional (easy to use) and easy to store.
Should not have
• Project must not include complex or obnoxious shapes and colours.

```html
<!DOCTYPE html>
<html lang="en">
<head>
<meta charset="utf-8">
<title>Herb &amp; Spice Pouch Range</title>
<link rel="stylesheet" href="https://fonts.googleapis.com/css2?family=Oswald:wght@400;600&display=swap">
<style>
  :root {
    --canvas: #000000;
    --band: #111111;
    --body-top: #3a3a38;
    --body-bottom: #5a5a57;
    --ink: #f4f1ea;
    --label-ink: #1a1a1a;
  }
  html, body {
    margin: 0;
    padding: 0;
    width: 1200px;
    height: 1200px;
    overflow: hidden;
    background: var(--canvas);
  }
  .range {
    position: relative;
    width: 1200px;
    height: 1200px;
  }
  .pouch {
    position: absolute;
    width: 390px;
    height: 600px;
  }
  .pouch--tea      { left: 28px;  top: 32px;
    --tone: #8f8a1f; --tone-light: #a8a22a; --window: #b89b05; --stripe: #e8c600;
    --content-a: #3b4222; --content-b: #6c6a3a; }
  .pouch--paprika  { left: 398px; top: 388px;
    --tone: #8a3322; --tone-light: #9a3d2a; --window: #7a2a1a; --stripe: #f05a1a;
    --content-a: #e2521c; --content-b: #f3a06a; }
  .pouch--tomatoes { left: 792px; top: 588px;
    --tone: #8a4a0e; --tone-light: #9a5614; --window: #7f430c; --stripe: #f07f1a;
    --content-a: #d8330f; --content-b: #f06a2a; }

  .pouch svg { display: block; width: 100%; height: 100%; }
  .pouch__top    { fill: var(--tone-light); }
  .pouch__wedge  { fill: var(--tone); }
  .pouch__body   { fill: url(#none); }
  .pouch__stripe { stroke: var(--stripe); stroke-width: 3.5; }
  .pouch__band   { fill: var(--band); }
  .pouch__window { fill: var(--window); }
  .pouch__mark   { fill: var(--stripe); }
  .stop-body-top    { stop-color: var(--body-top); }
  .stop-body-bottom { stop-color: var(--body-bottom); }
  .stop-content-a   { stop-color: var(--content-a); }
  .stop-content-b   { stop-color: var(--content-b); }

  .product-name {
    font-family: "Oswald", sans-serif;
    font-weight: 600;
    fill: var(--ink);
    letter-spacing: 1px;
  }
  .company-name {
    font-family: "Oswald", sans-serif;
    font-weight: 400;
    fill: var(--ink);
    font-size: 22px;
  }
  .weight {
    font-family: "Oswald", sans-serif;
    font-weight: 600;
    fill: var(--label-ink);
    font-size: 24px;
  }
</style>
</head>
<body>
<main class="range">

  <!-- Tea pouch -->
  <div class="pouch pouch--tea">
    <svg viewBox="0 0 390 600">
      <defs>
        <linearGradient id="tea-body" x1="0" y1="0" x2="0" y2="1">
          <stop offset="0" class="stop-body-top"/><stop offset="1" class="stop-body-bottom"/>
        </linearGradient>
        <radialGradient id="tea-content">
          <stop offset="0" class="stop-content-b"/><stop offset="1" class="stop-content-a"/>
        </radialGradient>
        <clipPath id="tea-shape"><path d="M0 0 H390 V560 Q390 570 380 572 L10 572 Q0 570 0 560 Z"/></clipPath>
      </defs>
      <g clip-path="url(#tea-shape)">
        <rect width="390" height="600" fill="url(#tea-body)"/>
        <rect class="pouch__top" width="390" height="180"/>
        <path class="pouch__wedge" d="M0 170 Q200 190 390 190 V300 Q200 210 0 250 Z"/>
        <path class="pouch__band" d="M0 132 Q200 100 390 118 V200 Q200 190 0 182 Z"/>
        <g class="pouch__stripes">
          <line class="pouch__stripe" x1="172" y1="0" x2="172" y2="104"/>
          <line class="pouch__stripe" x1="181" y1="0" x2="181" y2="104"/>
          <line class="pouch__stripe" x1="190" y1="0" x2="190" y2="104"/>
          <line class="pouch__stripe" x1="199" y1="0" x2="199" y2="104"/>
          <line class="pouch__stripe" x1="208" y1="0" x2="208" y2="104"/>
        </g>
        <text class="product-name" x="195" y="180" text-anchor="middle" font-size="50">TEA</text>
        <circle class="pouch__mark" cx="68" cy="262" r="12"/>
        <text class="company-name" x="102" y="258">COMPANY</text>
        <text class="company-name" x="102" y="286">NAME</text>
        <circle class="pouch__window" cx="195" cy="448" r="146"/>
        <ellipse cx="195" cy="430" rx="72" ry="110" fill="url(#tea-content)" role="img" aria-label="Window showing loose dried tea leaves"/>
        <text class="weight" x="100" y="552">10.58oz</text>
        <text class="weight" x="232" y="552">300g</text>
      </g>
    </svg>
  </div>

  <!-- Red paprika pouch -->
  <div class="pouch pouch--paprika">
    <svg viewBox="0 0 390 600">
      <defs>
        <linearGradient id="paprika-body" x1="0" y1="0" x2="0" y2="1">
          <stop offset="0" class="stop-body-top"/><stop offset="1" class="stop-body-bottom"/>
        </linearGradient>
        <radialGradient id="paprika-content">
          <stop offset="0" class="stop-content-b"/><stop offset="1" class="stop-content-a"/>
        </radialGradient>
        <clipPath id="paprika-shape"><path d="M0 0 H390 V560 Q390 570 380 572 L10 572 Q0 570 0 560 Z"/></clipPath>
      </defs>
      <g clip-path="url(#paprika-shape)">
        <rect width="390" height="600" fill="url(#paprika-body)"/>
        <rect class="pouch__top" width="390" height="180"/>
        <path class="pouch__wedge" d="M0 170 Q200 190 390 190 V300 Q200 210 0 250 Z"/>
        <path class="pouch__band" d="M0 132 Q200 100 390 118 V200 Q200 190 0 182 Z"/>
        <g class="pouch__stripes">
          <line class="pouch__stripe" x1="172" y1="0" x2="172" y2="104"/>
          <line class="pouch__stripe" x1="181" y1="0" x2="181" y2="104"/>
          <line class="pouch__stripe" x1="190" y1="0" x2="190" y2="104"/>
          <line class="pouch__stripe" x1="199" y1="0" x2="199" y2="104"/>
          <line class="pouch__stripe" x1="208" y1="0" x2="208" y2="104"/>
        </g>
        <text class="product-name" x="195" y="172" text-anchor="middle" font-size="46">RED PAPRICA</text>
        <circle class="pouch__mark" cx="68" cy="262" r="12"/>
        <text class="company-name" x="102" y="258">COMPANY</text>
        <text class="company-name" x="102" y="286">NAME</text>
        <circle class="pouch__window" cx="195" cy="448" r="146"/>
        <ellipse cx="195" cy="430" rx="72" ry="110" fill="url(#paprika-content)" role="img" aria-label="Window showing dried red paprika flakes"/>
        <text class="weight" x="100" y="552">10.58oz</text>
        <text class="weight" x="232" y="552">300g</text>
      </g>
    </svg>
  </div>

  <!-- Tomatoes pouch -->
  <div class="pouch pouch--tomatoes">
    <svg viewBox="0 0 390 600">
      <defs>
        <linearGradient id="tomatoes-body" x1="0" y1="0" x2="0" y2="1">
          <stop offset="0" class="stop-body-top"/><stop offset="1" class="stop-body-bottom"/>
        </linearGradient>
        <radialGradient id="tomatoes-content">
          <stop offset="0" class="stop-content-b"/><stop offset="1" class="stop-content-a"/>
        </radialGradient>
        <clipPath id="tomatoes-shape"><path d="M0 0 H390 V560 Q390 570 380 572 L10 572 Q0 570 0 560 Z"/></clipPath>
      </defs>
      <g clip-path="url(#tomatoes-shape)">
        <rect width="390" height="600" fill="url(#tomatoes-body)"/>
        <rect class="pouch__top" width="390" height="180"/>
        <path class="pouch__wedge" d="M0 170 Q200 190 390 190 V300 Q200 210 0 250 Z"/>
        <path class="pouch__band" d="M0 132 Q200 100 390 118 V200 Q200 190 0 182 Z"/>
        <g class="pouch__stripes">
          <line class="pouch__stripe" x1="172" y1="0" x2="172" y2="104"/>
          <line class="pouch__stripe" x1="181" y1="0" x2="181" y2="104"/>
          <line class="pouch__stripe" x1="190" y1="0" x2="190" y2="104"/>
          <line class="pouch__stripe" x1="199" y1="0" x2="199" y2="104"/>
          <line class="pouch__stripe" x1="208" y1="0" x2="208" y2="104"/>
        </g>
        <text class="product-name" x="195" y="172" text-anchor="middle" font-size="48">TOMATOES</text>
        <circle class="pouch__mark" cx="68" cy="262" r="12"/>
        <text class="company-name" x="102" y="258">COMPANY</text>
        <text class="company-name" x="102" y="286">NAME</text>
        <circle class="pouch__window" cx="195" cy="448" r="146"/>
        <ellipse cx="195" cy="430" rx="72" ry="110" fill="url(#tomatoes-content)" role="img" aria-label="Window showing red tomato powder"/>
        <text class="weight" x="100" y="552">10.58oz</text>
        <text class="weight" x="232" y="552">300g</text>
      </g>
    </svg>
  </div>

</main>
</body>
</html>
```